Photo/Video Company needs a business card design

We need a business card design for a photo/video production company called 'Brightwave Studios'. We primarily do wedding photography and videography, however we also do commercial, corporate, and promo work.

We would like a clean, white design that primarily markets us as a wedding photo/video company, but still sleek enough that we attract corporate and commercial clients.

Industry/Entity Type

Wedding

Requirements
Must have
• We wish the front of the business card to simply have the logo, and the back will have the contact information:

Brightwave Studios
Wedding, Event, Corporate, Commercial, Promo
647-518-2736
info@brightwavestudios.example
www.brightwavestudios.example

We are hoping for a version of the card that has only the companies name on it, as well as several variations that have different employees names printed.

The employee names and titles are:

Teo Lindqvar - Photo/Video
Dilan Lindqvar - Photo/Video
Pieter Kalbrook -Video
Odile Brunvik -Photo/Video

The design should use similar fonts in the writing as the fonts used in the logo design. The AI file will be provided.
Nice to have
• We also might like to see the front of the card have the main logo, as well as 'Wedding, Event, Corporate, Commercial, Promo' written in the bottom corner.
Should not have
• No old style fonts should be used. Also no other graphic images should be created, but we are open to the possibility of having shapes and borders.

```html
<!DOCTYPE html>
<html lang="en">
<head>
<meta charset="utf-8">
<title>Brightwave Studios — Business Card</title>
<link rel="stylesheet" href="https://fonts.googleapis.com/css2?family=Questrial&display=swap">
<style>
  :root {
    --brand-red: #d8232a;
    --ink: #333638;
    --ink-soft: #55595c;
    --paper: #ffffff;
    --paper-shade: #e9ebed;
  }
  * { margin: 0; padding: 0; box-sizing: border-box; }
  html, body {
    width: 1051px;
    height: 1200px;
    overflow: hidden;
    background: var(--paper);
    font-family: "Questrial", "Century Gothic", sans-serif;
    color: var(--ink);
  }
  .canvas {
    position: relative;
    width: 1051px;
    height: 1200px;
  }
  .card-side {
    position: absolute;
    left: 0;
    width: 1051px;
    height: 600px;
    background: radial-gradient(ellipse at 50% 45%, var(--paper) 55%, var(--paper-shade) 100%);
  }
  .card-back { top: 0; }
  .card-front { top: 600px; }

  .wordmark {
    position: absolute;
    display: flex;
    align-items: center;
    gap: 22px;
    color: var(--brand-red);
    text-transform: uppercase;
    white-space: nowrap;
    line-height: 1;
  }
  .wordmark-square {
    width: 58px;
    height: 58px;
    background: var(--brand-red);
  }
  .card-back .wordmark {
    left: 170px;
    top: 165px;
    font-size: 62px;
  }
  .card-front .wordmark {
    left: 0;
    right: 0;
    justify-content: center;
    top: 310px;
    font-size: 66px;
  }

  .company-name {
    position: absolute;
    left: 300px;
    top: 305px;
    font-size: 40px;
    color: var(--brand-red);
  }
  .services {
    position: absolute;
    left: 300px;
    top: 350px;
    font-size: 27px;
    color: var(--ink);
  }
  .contact-list {
    position: absolute;
    left: 300px;
    top: 400px;
    list-style: none;
  }
  .contact-list li {
    display: flex;
    align-items: baseline;
    height: 30px;
  }
  .contact-label {
    width: 125px;
    text-align: right;
    font-size: 17px;
    color: var(--ink-soft);
  }
  .contact-value {
    font-size: 27px;
    color: var(--ink);
  }
  .contact-value::before {
    content: "•";
    margin: 0 10px 0 8px;
  }

  .logo-glow {
    position: absolute;
    left: 325px;
    top: 395px;
    width: 400px;
    height: 18px;
    border-radius: 50%;
    background: radial-gradient(ellipse at center, rgba(216,35,42,0.18) 0%, rgba(216,35,42,0) 70%);
  }
  .service-strip {
    position: absolute;
    left: 0;
    right: 0;
    top: 500px;
    text-align: center;
    font-size: 23px;
    color: var(--ink);
    letter-spacing: 0.5px;
  }
  .service-strip .divider {
    color: var(--brand-red);
    margin: 0 10px;
  }
</style>
</head>
<body>
<main class="canvas">
  <section class="card-side card-back" aria-label="Card back with contact details">
    <div class="wordmark"><span class="wordmark-square"></span>Brightwave Studios</div>
    <p class="company-name">Brightwave Studios</p>
    <p class="services">Wedding, Event, Corporate, Commercial, Promo</p>
    <ul class="contact-list">
      <li><span class="contact-label">phone</span><span class="contact-value">647-518-2736</span></li>
      <li><span class="contact-label">email</span><span class="contact-value">info@brightwavestudios.example</span></li>
      <li><span class="contact-label">website</span><span class="contact-value">www.brightwavestudios.example</span></li>
    </ul>
  </section>

  <section class="card-side card-front" aria-label="Card front with company name">
    <div class="wordmark"><span class="wordmark-square"></span>Brightwave Studios</div>
    <div class="logo-glow"></div>
    <p class="service-strip">wedding<span class="divider">|</span>event<span class="divider">|</span>corporate<span class="divider">|</span>commercial<span class="divider">|</span>prom</p>
  </section>
</main>
</body>
</html>
```